Health Coaching Flyer for New Clients

I need a two-sided flyer (3.5" x 8.5" preferred or 5" x 7") to distribute to potential coaching clients. My business name is Talvery Health & Wellness Coaching. My business is focused on helping people with habit changes that contribute to their overall well-being. I would like the design colors to be gender neutral. I would like a small photo of myself near the "my name is Joan" statement. Please feel free to change the logo color to match the design.

Target Market(s)

Adults of all ages.

Font styles to use
Serif

Requirements
Must have
• Emphasize my opening question (found in health coaching brochure - attached).
• Small picture of myself near "my name is Joan" statement.
Should not have
• No light of pastel colors.

```html
<!DOCTYPE html>
<html lang="en">
<head>
<meta charset="utf-8">
<title>Talvery Health &amp; Wellness Coaching – New Client Flyer</title>
<link href="https://fonts.googleapis.com/css2?family=Montserrat:wght@600;700;800&family=Didact+Gothic&display=swap" rel="stylesheet">
<style>
  :root {
    --backdrop: #d6d6d6;
    --teal-deep: #13888a;
    --teal-mid: #2aa3a3;
    --teal-sky: #5fb9b8;
    --sky-top: #3e7f92;
    --paper: #f4f4f2;
    --ink: #2a2a2a;
    --gold: #f1cb3a;
    --white: #ffffff;
    --portrait: #8a5a48;
  }
  * { margin: 0; padding: 0; box-sizing: border-box; }
  html, body { width: 1200px; height: 1200px; overflow: hidden; }
  body { background: var(--backdrop); position: relative; font-family: "Didact Gothic", sans-serif; }

  .flyer { position: absolute; top: 240px; width: 540px; height: 700px; overflow: hidden; box-shadow: 0 8px 24px rgba(0,0,0,.18); }
  .flyer--front { left: 40px; background: var(--paper); }
  .flyer--back { left: 620px; background: linear-gradient(180deg, var(--teal-deep) 0%, var(--teal-mid) 40%, #bfdedd 68%, var(--paper) 85%); }

  /* front */
  .hero-scene { position: absolute; left: 0; top: 0; width: 540px; height: 360px;
    background: linear-gradient(180deg, var(--sky-top) 0%, var(--teal-sky) 45%, #5aa79f 75%, #4f7f6c 100%); }
  .headline { position: absolute; left: 34px; top: 92px; width: 480px; font-family: "Montserrat", sans-serif; font-weight: 800; text-transform: uppercase; line-height: 1.18; }
  .headline__lead { display: block; color: var(--gold); font-size: 34px; }
  .headline__rest { display: block; color: var(--white); font-size: 21px; font-weight: 700; }
  .headline__rest span { display: block; text-align: right; }
  .portrait { position: absolute; left: 30px; top: 250px; width: 200px; height: 230px; background: linear-gradient(160deg, #b7a38f, var(--portrait) 60%, #3a2a25); }
  .intro { position: absolute; z-index: 1; left: 30px; top: 372px; width: 484px; font-family: "Montserrat", sans-serif; font-weight: 700; font-size: 12.5px; line-height: 1.5; color: var(--ink); letter-spacing: .3px; }
  .intro__float { float: left; width: 210px; height: 114px; }
  .front-band { position: absolute; left: 0; bottom: 0; width: 540px; height: 110px; background: linear-gradient(180deg, var(--paper) 0%, var(--teal-mid) 55%, var(--teal-deep) 100%); }

  /* back */
  .benefits { position: absolute; left: 36px; top: 40px; width: 468px; color: var(--white); text-transform: uppercase; font-size: 13.5px; letter-spacing: 1.2px; line-height: 1.35; }
  .benefits__title { font-family: "Montserrat", sans-serif; font-weight: 700; font-size: 21px; letter-spacing: 1.5px; margin-bottom: 16px; }
  .benefits__list { list-style: none; }
  .benefits__list li { margin-bottom: 13px; }
  .invite { position: absolute; left: 36px; top: 388px; width: 468px; color: var(--teal-deep); text-transform: uppercase; font-size: 13.5px; letter-spacing: 1.2px; line-height: 1.35; }
  .invite p { margin-bottom: 16px; }
  .offer { font-family: "Montserrat", sans-serif; font-weight: 700; font-size: 23px; text-align: center; text-decoration: underline; margin: -8px 0 20px; }
  .closing { text-align: center; }
  .signature { position: absolute; right: 36px; bottom: 32px; text-align: right; color: var(--teal-deep); text-transform: uppercase; letter-spacing: 1.2px; }
  .signature__name { font-family: "Montserrat", sans-serif; font-weight: 700; font-size: 20px; }
  .signature__line { font-size: 13px; }
  .signature__email { font-size: 13px; text-decoration: underline; }
</style>
</head>
<body>
  <section class="flyer flyer--front">
    <div class="hero-scene" role="img" aria-label="Raised hands meeting in a high five against a sunlit mountain sky"></div>
    <h1 class="headline">
      <span class="headline__lead">Need support</span>
      <span class="headline__rest">In making real, lasting lifestyle<span>and behavior changes?</span></span>
    </h1>
    <div class="portrait" role="img" aria-label="Small portrait photo of Joan, the coach"></div>
    <p class="intro"><span class="intro__float"></span>My name is Joan. I am studying to become a THRIVE-Certified Functional Health Coach. My training involves many science-based practices that improve both our health and how we grow and change as humans. I now have the opportunity to turn that knowledge into practice by coaching actual clients interested in improving their own health and well-being.</p>
    <div class="front-band"></div>
  </section>

  <section class="flyer flyer--back">
    <div class="benefits">
      <h2 class="benefits__title">Functional health coaches...</h2>
      <ul class="benefits__list">
        <li>Build on your strengths rather than focus on your weaknesses.</li>
        <li>Guide you in finding your own strategies and motivation for change.</li>
        <li>Provide a judgment-free zone and support your progress.</li>
        <li>Use an experimental mindset to find and develop new, lasting habits.</li>
        <li>Serve as an accountability partner as you reach your health goals, whether they be sleep, diet, fitness, social connection, or stress.</li>
      </ul>
    </div>
    <div class="invite">
      <p>I invite you to participate with me as I continue to hone my coaching skills. We can develop a plan and schedule that aligns with your goals.</p>
      <p>As a way to give back to my community, I am offering new clients six free coaching sessions.</p>
      <p class="offer">This is a limited time offer.</p>
      <p class="closing">Please contact me.<br>I'm ready to support you as you work to improve your health.</p>
    </div>
    <div class="signature">
      <div class="signature__name">Joan Talvery</div>
      <div class="signature__line">555-014-2290</div>
      <div class="signature__email">talveryhwc@example.com</div>
    </div>
  </section>
</body>
</html>
```